ko rim magazine

just need coupons of real customers made for my magazine, I have the layout or temp lets of the magazine i just need the coupons to be made and plug-in. i have examples, of the ads or coupons, I'm sure they will need to redone. and in a section of the magazine their in a church directory. with this section , i need the pic of the pastor plug in with their church information and in do have some ex-samples of that as well. with the websites of the businesses. if you need to grab an image from their site . you'll be able to do so. all of the business are in the upload section , these are small base business so a lot of the ads and logos need redone any way . so i will look at it and let you know.

P.S with the new coupons and logos I'm trying to impress these customers to stay with the magazine

Target Market(s)

small businesses

Requirements
Must have
• good graphics
Should not have
• not pixelated graphics

```html
<!DOCTYPE html>
<html lang="en">
<head>
<meta charset="utf-8">
<title>ko rim magazine – Church Directory</title>
<link href="https://fonts.googleapis.com/css2?family=Poppins:wght@400;500;600;700&family=Libre+Baskerville:ital,wght@0,400;0,700;1,400;1,700&family=Oswald:wght@500;600&display=swap" rel="stylesheet">
<style>
:root{
  --ink:#1d1d1f;
  --navy-dark:#141c33;
  --cedar-grey:#ececec;
  --cedar-orange:#f7941d;
  --redemption-pink:#f3d8cf;
  --beacon-bg:#e7eaf5;
  --beacon-blue:#24368f;
  --grace-bg:#f6f5ef;
  --grace-wave:#e4e1d1;
  --word-green:#a9bf98;
  --opendoor-red:#c1272d;
  --charcoal:#231f20;
  --bethesda-bg:#cfd6e4;
  --cornerstone-red:#e42d2d;
  --fulton-brown:#b4653f;
  --fulton-band:#94492a;
  --stmark-pink:#fbdce2;
  --paper:#ffffff;
}
*{margin:0;padding:0;box-sizing:border-box}
html,body{width:848px;height:1200px;overflow:hidden;background:var(--paper)}
body{font-family:"Poppins",sans-serif;color:var(--ink);position:relative}
.card{position:absolute;width:390px;height:214px;overflow:hidden;border:1px solid #2a2a2a}
.col-l{left:24px}.col-r{left:433px}
.row1{top:24px}.row2{top:258px}.row3{top:493px}.row4{top:727px}.row5{top:962px}
.abs{position:absolute}
.photo{position:absolute}
.rule{position:absolute;height:1px;background:currentColor}

/* Cedar Grove */
.cedar{background:var(--cedar-grey)}
.cedar .band{left:0;top:74px;width:100%;height:107px;background:var(--cedar-orange)}
.cedar .foot{left:0;top:181px;width:100%;height:33px;background:var(--navy-dark);color:#fff;font-size:8.4px;letter-spacing:1.2px;text-align:center;line-height:13px;padding-top:3px}
.cedar .name{left:16px;top:17px;font-size:14.4px;font-weight:600;line-height:17px}
.cedar .sub{left:16px;top:54px;font-size:8.6px;letter-spacing:1px}
.cedar .info{left:14px;font-size:8.2px;line-height:11px}
.cedar .photo{left:244px;top:11px;width:130px;height:130px;border-radius:50%;border:2px solid var(--navy-dark);background:radial-gradient(circle at 50% 40%,#6b4a3a 0 28%,#f2f2f2 29%)}
.cedar .rev{left:240px;top:146px;width:140px;text-align:center;font-size:9.6px;font-weight:600;line-height:12.5px}

/* Redemption */
.redemption{background:var(--redemption-pink)}
.redemption .photo{left:0;top:0;width:134px;height:214px;background:linear-gradient(180deg,#f4f4f4 0 45%,#8a5a3a 45% 100%)}
.redemption .panel{left:134px;top:0;width:256px;height:214px;border-left:1px solid #333;text-align:center}
.redemption h2{position:absolute;left:0;right:0;top:17px;font-size:24px;font-style:italic;font-weight:600;line-height:29px}
.redemption .rule{left:50px;width:156px;background:#333}
.redemption p{position:absolute;left:0;right:0;font-size:11.5px;line-height:15px}

/* Beacon Hill */
.beacon{background:var(--beacon-bg)}
.beacon h2{position:absolute;left:18px;top:11px;color:#fff;font-size:20px;font-weight:600;z-index:2}
.beacon .photo{left:271px;top:42px;width:119px;height:135px;background:linear-gradient(180deg,#c9ccd6 0 20%,#5a3d2e 20% 48%,#1d2440 48%)}
.beacon .pastor{left:20px;top:75px;font-size:15.5px;font-weight:600}
.beacon .time{left:20px;top:97px;font-size:11.5px}
.beacon .phone{left:20px;top:136px;font-size:28px;font-weight:400;letter-spacing:.5px}
.beacon .foot{left:0;top:177px;width:100%;height:37px;background:var(--navy-dark);color:#fff;font-size:13px;display:flex;align-items:center;justify-content:center;gap:6px}

/* Grace Temple */
.grace{background:var(--grace-bg);font-family:"Libre Baskerville",serif}
.grace .photo{left:12px;top:36px;width:136px;height:151px;background:linear-gradient(90deg,#2a2d3c 0 45%,#2f6d56 45%)}
.grace h2{position:absolute;right:16px;top:12px;text-align:right;font-size:17px;font-weight:400;line-height:22px}
.grace .addr{right:15px;top:93px;text-align:right;font-family:"Poppins",sans-serif;font-size:11.5px;line-height:15px}
.grace .svc{right:15px;top:148px;text-align:right;font-family:"Poppins",sans-serif;font-size:9.8px;line-height:13px}
.grace .foot{left:0;top:187px;width:100%;height:27px;background:var(--charcoal);color:#fff;font-size:15px;text-align:center;line-height:27px;padding-left:50px}

/* Word Center */
.word{background:var(--paper)}
.word .panel{left:0;top:0;width:278px;height:214px;background:var(--word-green);text-align:center;letter-spacing:.6px}
.word h2{position:absolute;left:0;right:0;top:14px;font-size:20px;font-weight:700;letter-spacing:1.6px}
.word p{position:absolute;left:0;right:0;font-size:10.8px;line-height:14.5px}
.word .rule{left:20px;width:236px;background:#222}
.word h3{position:absolute;left:0;right:0;top:101px;font-size:18px;font-weight:700;letter-spacing:1.4px}
.word .photo{left:278px;top:0;width:112px;height:214px;background:linear-gradient(180deg,#f7f7f7 0 18%,#4a3024 18% 42%,#262b3a 42%)}

/* Open Door */
.opendoor{background:var(--paper);font-family:"Libre Baskerville",serif}
.opendoor .top{left:0;top:0;width:100%;height:110px;background:var(--charcoal)}
.opendoor .red{left:26px;top:0;width:132px;height:214px;background:var(--opendoor-red)}
.opendoor .photo{left:16px;top:22px;width:148px;height:148px;border-radius:50%;border:2px solid #fff;background:linear-gradient(90deg,#e8e6e1 0 50%,#2c4d55 50%)}
.opendoor .caption{left:26px;top:174px;width:132px;text-align:center;color:#fff;font-size:9.6px;font-style:italic;font-weight:700;line-height:15px}
.opendoor h2{position:absolute;right:20px;top:14px;text-align:right;color:#fff;font-size:19px;font-style:italic;font-weight:700;line-height:25px}
.opendoor .addr{right:22px;top:71px;text-align:right;color:#fff;font-size:9.4px;line-height:13px}
.opendoor .svc-h{right:22px;top:129px;color:var(--opendoor-red);font-size:12.5px;font-style:italic}
.opendoor .svc{right:22px;top:156px;text-align:right;font-size:10.6px;line-height:15.5px}

/* Bethesda */
.bethesda{background:var(--bethesda-bg)}
.bethesda svg{position:absolute;left:0;top:0}
.bethesda .photo{left:22px;top:20px;width:122px;height:194px;background:linear-gradient(180deg,#5a3b2c 0 24%,#c7c3bb 24%)}
.bethesda h2{position:absolute;right:18px;top:14px;text-align:right;font-size:18.5px;font-weight:400;letter-spacing:1.2px;line-height:24px}
.bethesda .rule{right:20px;width:54px;background:#222}
.bethesda p{position:absolute;right:18px;text-align:right;font-size:12.4px;line-height:17px}

/* Cornerstone */
.cornerstone{background:var(--paper)}
.cornerstone .bishop{left:18px;top:18px;font-size:17px;font-weight:500;line-height:20px;letter-spacing:-.3px}
.cornerstone .svc{left:0;top:66px;width:270px;height:16px;background:linear-gradient(90deg,#f2a6a6 0,#f7c9c9 60%,rgba(255,255,255,0));padding-left:18px;font-size:10.5px;line-height:16px;color:#222}
.cornerstone .addr{left:18px;top:88px;font-size:10.6px;line-height:15.5px}
.cornerstone .photo{left:223px;top:24px;width:167px;height:120px;background:linear-gradient(180deg,#f1f1f1 0 8%,#6d4433 8% 70%,var(--cornerstone-red) 70%);clip-path:polygon(20% 0,90% 0,100% 30%,100% 100%,0 100%)}
.cornerstone svg{position:absolute;left:0;top:0}
.cornerstone .brand{left:0;right:0;top:172px;text-align:center;color:#fff;font-size:18px;font-weight:400;white-space:nowrap}

/* Fulton Street */
.fulton{background:#1f1f22}
.fulton .panel{left:0;top:0;width:260px;height:214px;background:var(--fulton-brown);color:#fff;text-align:center}
.fulton h2{position:absolute;left:0;right:0;top:12px;font-family:"Oswald",sans-serif;font-weight:600;font-size:17px;line-height:20px;letter-spacing:.2px}
.fulton p{position:absolute;left:0;right:0;font-size:10.6px;line-height:13.5px}
.fulton svg{position:absolute;left:0;top:0}
.fulton .photo{left:260px;top:10px;width:130px;height:160px;background:linear-gradient(180deg,#1f1f22 0 10%,#5b3a2c 10% 48%,#2d2d33 48%)}
.fulton .rev{left:260px;top:169px;width:130px;text-align:center;color:#fff;font-size:10.6px;line-height:14px}

/* St. Mark */
.stmark{background:var(--stmark-pink)}
.stmark .photo{left:0;top:0;width:160px;height:214px;background:linear-gradient(180deg,#f7f7f7 0 12%,#3b2a26 12% 50%,#1c1c1f 50% 70%,#c4202a 70%)}
.stmark .body{left:160px;top:0;width:230px;height:214px;text-align:center}
.stmark h2{position:absolute;left:0;right:0;top:20px;font-size:17px;font-weight:700;transform:rotate(-2deg)}
.stmark p{position:absolute;left:0;right:0;font-size:9.2px;line-height:12.5px}
.stmark .rule{left:90px;width:54px;background:#222}
</style>
</head>
<body>

<section class="card col-l row1 cedar">
  <div class="abs band"></div>
  <div class="abs name">Cedar Grove Community<br>Missionary Baptist Church</div>
  <div class="abs sub">SUNDAY WORSHIP SERVICE</div>
  <div class="abs info" style="top:84px">IN-PERSON SUNDAY WORSHIP SERVICE<br>9:00AM &amp; REPLAY 6:00PM EST</div>
  <div class="abs info" style="top:117px;font-weight:500">Wednesday, Midweek Only Bible Study:<br><span style="font-weight:400">2:00AM - 1:00PM</span></div>
  <div class="abs info" style="top:148px;font-weight:500">Midweek Corporate Prayer:<br><span style="font-weight:400">6:00PM - 7:00PM</span></div>
  <div class="photo" role="img" aria-label="Portrait of the reverend"></div>
  <div class="abs rev">Reverend<br>Harold D. Whitfield</div>
  <div class="abs foot">4120 MAPLECREST AVENUE PITTSBURGH, PA 15208<br>412.555.0171 - CHURCH &nbsp;|&nbsp; 412.555.0172 - FAX</div>
</section>

<section class="card col-r row1 redemption">
  <div class="photo" role="img" aria-label="Pastor preaching at a wooden pulpit"></div>
  <div class="abs panel">
    <h2>Redemption<br>Baptist Church</h2>
    <div class="rule" style="top:88px"></div>
    <p style="top:101px">318 Larkwood Ave, Pittsburgh, PA<br>(412) 555 - 0128</p>
    <div class="rule" style="top:143px"></div>
    <p style="top:163px;font-size:13.5px;font-weight:600">Dr. Marcus W. Ellison Sr.</p>
    <p style="top:181px;font-size:10.6px">Church Service Sunday 11am</p>
  </div>
</section>

<section class="card col-l row2 beacon">
  <svg width="390" height="52" viewBox="0 0 390 52" aria-hidden="true"><path d="M0 0H318L296 40Q290 50 278 50H0Z" fill="var(--beacon-blue)"/></svg>
  <h2>Beacon Hill Baptist Church</h2>
  <div class="abs pastor">Dr. Warren R. Gaines</div>
  <div class="abs time">Sunday Worship Service 10:30 AM</div>
  <div class="abs phone">(412) 555 - 0143</div>
  <div class="photo" role="img" aria-label="Portrait of the pastor in a suit"></div>
  <div class="abs foot">
    <svg width="14" height="17" viewBox="0 0 14 17" aria-hidden="true"><path d="M7 0A7 7 0 0 0 0 7C0 12 7 17 7 17S14 12 14 7A7 7 0 0 0 7 0Z" fill="#fff"/><circle cx="7" cy="7" r="2.6" fill="var(--navy-dark)"/></svg>
    7510 Orchard Street Pittsburgh, PA 15208
  </div>
</section>

<section class="card col-r row2 grace">
  <svg class="abs" style="left:0;top:0" width="390" height="214" viewBox="0 0 390 214" aria-hidden="true"><path d="M150 70C230 95 300 40 390 55V187H150Z" fill="var(--grace-wave)"/></svg>
  <div class="photo" role="img" aria-label="Pastor couple standing together"></div>
  <h2>Grace Temple Church<br>Pittsburgh (gtc-pgh)</h2>
  <div class="abs addr">2915 LINDEN STREET,<br>PITTSBURGH, PA. 15208<br>(412) 555 - 0156</div>
  <div class="abs svc">SUNDAY WORSHIP SERVICE AT<br>8AM &amp; 10:45AM</div>
  <div class="abs foot">Reverend Ronald | Alicia Boyd</div>
</section>

<section class="card col-l row3 word">
  <div class="abs panel">
    <h2>Word Center Church</h2>
    <p style="top:43px">Word Center Church / 540 N. FAIRVIEW<br>AVE. / PITTSBURGH, PA 15208<br>(412) 555 - 0164</p>
    <div class="rule" style="top:96px"></div>
    <h3>Pastor</h3>
    <p style="top:128px;font-size:14px;letter-spacing:0">Reverend Dr. James R. Whitman Jr.</p>
    <div class="rule" style="top:158px"></div>
    <p style="top:172px">Sunday Worship Service<br>Sundays @ 10am</p>
  </div>
  <div class="photo" role="img" aria-label="Portrait of the pastor in a suit"></div>
</section>

<section class="card col-r row3 opendoor">
  <div class="abs top"></div>
  <div class="abs red"></div>
  <div class="photo" role="img" aria-label="Apostle and pastor posing before a cross"></div>
  <div class="abs caption">Apostle Clarence &amp;<br>Pastor Mara Lowe</div>
  <h2>Open Door<br>Christian Fellowship</h2>
  <div class="abs addr">2204 Ashford Street Pittsburgh, PA<br>(412) 555 - 0179</div>
  <div class="abs svc-h">Sunday Worship Service</div>
  <div class="abs svc">Sunday Service At 11:00 Am<br>Wednesday Bible Study At 7:30 Pm<br>Saturday Prayer At 9:00 Am</div>
</section>

<section class="card col-l row4 bethesda">
  <svg width="390" height="214" viewBox="0 0 390 214" aria-hidden="true"><path d="M0 0H110C170 30 170 180 135 214H0Z" fill="#fff"/></svg>
  <div class="photo" role="img" aria-label="Portrait of the pastor in a grey blazer"></div>
  <h2>BETHESDA<br>BAPTIST CHURCH</h2>
  <div class="rule" style="top:74px"></div>
  <p style="top:93px;font-weight:600;font-size:11.8px">REVEREND DR. ROLAND A. PIERCE</p>
  <p style="top:111px">Church Service Sunday 11am</p>
  <div class="rule" style="top:147px"></div>
  <p style="top:162px">(412) 555 - 0185<br>1830 Hillcrest Ave, Pittsburgh, PA</p>
</section>

<section class="card col-r row4 cornerstone">
  <div class="abs bishop">BISHOP<br>DENNIS OWEN CARTER, JR</div>
  <div class="abs svc">SUNDAY WORSHIP SERVICE 10:30AM</div>
  <div class="abs addr">412 WESTBROOK DR, PITTSBURGH, PA,<br>PHONE: (412) 555 - 0192</div>
  <div class="photo" role="img" aria-label="Portrait of the bishop in glasses"></div>
  <svg width="390" height="214" viewBox="0 0 390 214" aria-hidden="true"><path d="M0 160Q40 140 120 136Q280 128 330 150Q375 130 390 135V214H0Z" fill="var(--charcoal)"/></svg>
  <div class="abs brand">Cornerstone International Ministries</div>
</section>

<section class="card col-l row5 fulton">
  <div class="abs panel">
    <h2>FULTON STREET<br>MISSIONARY BAPTIST CHURCH</h2>
    <p style="top:59px">(412) 555 - 0107<br>5020 Fulton St. Pittsburgh, PA</p>
    <svg width="260" height="214" viewBox="0 0 260 214" aria-hidden="true"><path d="M0 106Q130 84 260 106V122Q130 100 0 124Z" fill="var(--fulton-band)"/></svg>
    <p style="top:100px;font-weight:600;font-size:11.5px;transform:rotate(-2deg)">Church Service, Join Us Virtually</p>
    <p style="top:129px;font-size:10px;line-height:13px">Sunday Academy 7:30am<br>Sunday Worship 9:00am, 2:00pm<br>7:00pm, 10:00pm<br>Mondays 8:00am and 12 noon<br>Wednesdays at Noon<br>Saturdays at 10:00pm</p>
  </div>
  <div class="photo" role="img" aria-label="Portrait of the reverend in a suit"></div>
  <div class="abs rev">Reverend<br>Dr. Derrick T. Coleman</div>
</section>

<section class="card col-r row5 stmark">
  <div class="photo" role="img" aria-label="Pastor speaking at a pulpit"></div>
  <div class="abs body">
    <h2>St. Mark Baptist Church</h2>
    <p style="top:56px">ST. MARK BAPTIST CHURCH<br>4410 RIDGE AVE. PITTSBURGH, PA</p>
    <p style="top:84px;font-size:12.8px">(412) 555 - 0119</p>
    <div class="rule" style="top:110px"></div>
    <p style="top:120px;font-size:11.5px;font-weight:600;line-height:16px">PASTOR,<br>REV. DENISE HOLLOWAY</p>
    <p style="top:170px">SUNDAY WORSHIP SERVICE @ 10:30AM<br>SUNDAY SCHOOL 8:30AM</p>
  </div>
</section>

</body>
</html>
```